Optometrist/Eye Care Clinic Business card with new logo attached

We are a small, independent eye care clinic in Canada. We have recently updated our logo (as attached), and would like a professional, modern and health care oriented business card to highlight our office details and our optometrist. We'd like to incorporate the blue colours as seen on our logo.

Target Market(s)

demographic: age 35-65 male/female equal

Industry/Entity Type

Health Care

Contact Information for Business Card

Name of clinic: "Marrow Bend Eye Care Optometry"

Font styles to use
Sans Serif

Colors
0355a3

Requirements
Must have
• our website: marrowbendeyecare.com
• Dr Lena Quorvik
• Optometrist
• 217-392 E Halvering Ave
• Vancouver BC V6R 3J8
• P: 604-319-2058
• E: info@marrowbendeyecare.com
Nice to have
• front side: logo/name of clinic as seen on logo attached and website
• backside: logo on the left side, and name/title/address/phone/email

```html
<!DOCTYPE html>
<html lang="en">
<head>
<meta charset="utf-8">
<title>Marrow Bend Eye Care Optometry – Business Card</title>
<link rel="stylesheet" href="https://fonts.googleapis.com/css2?family=Open+Sans:wght@300;400;600;700&display=swap">
<style>
  :root {
    --backdrop: #b4b4b4;
    --card: #ffffff;
    --navy: #123f5e;
    --brand-blue: #0355a3;
    --teal: #1e8bb5;
    --bar: #0d4c92;
    --ink: #3a3a3a;
    --divider: #9fc6dc;
  }
  * { margin: 0; padding: 0; box-sizing: border-box; }
  html, body {
    width: 1200px; height: 1138px; overflow: hidden;
    background: var(--backdrop);
    font-family: "Open Sans", Arial, sans-serif;
  }
  .canvas { position: relative; width: 1200px; height: 1138px; }
  .card {
    position: absolute; left: 250px; width: 730px;
    background: var(--card); overflow: hidden;
  }
  .card--contact { top: 163px; height: 416px; }
  .card--brand { top: 601px; height: 421px; }

  /* clinic name */
  .clinic-name {
    position: absolute; color: var(--navy); font-weight: 400;
    text-transform: uppercase; line-height: 1.25;
  }
  .card--contact .clinic-mark {
    position: absolute; left: 546px; top: 22px; width: 112px; height: 112px;
    border-radius: 50%; background: var(--navy);
  }
  .card--contact .clinic-name {
    right: 36px; top: 142px; text-align: right;
    font-size: 17px; letter-spacing: 3px;
  }

  /* person */
  .person-name {
    position: absolute; left: 37px; top: 199px;
    font-size: 24px; font-weight: 700; color: var(--navy); letter-spacing: 0.2px;
  }
  .person-title {
    position: absolute; left: 37px; top: 232px;
    font-size: 21px; font-weight: 300; color: var(--brand-blue);
  }
  .rule-strong {
    position: absolute; left: 37px; top: 266px; width: 159px; height: 6px;
    background: var(--bar);
  }
  .rule-thin {
    position: absolute; left: 196px; top: 268px; right: 0; height: 2px;
    background: var(--teal);
  }

  /* contact list */
  .contact {
    position: absolute; display: flex; align-items: center; gap: 6px;
    font-size: 16.5px; line-height: 22px; color: var(--ink); white-space: nowrap;
  }
  .contact svg { width: 15px; height: 15px; flex: none; }
  .contact--phone { left: 37px; top: 304px; font-size: 18px; }
  .contact--email { left: 37px; top: 334px; }
  .contact--web { left: 37px; top: 363px; }
  .contact-divider {
    position: absolute; left: 332px; top: 338px; width: 1px; height: 43px;
    background: var(--divider);
  }
  .contact--address {
    left: 348px; top: 334px; align-items: flex-start;
    font-size: 17.5px; letter-spacing: 0.6px;
  }
  .contact--address svg { margin-top: 4px; }
  .contact--address span { line-height: 29px; display: block; margin-top: -3px; }
  .card-band {
    position: absolute; left: 0; right: 0; bottom: 0; height: 13px;
    background: var(--bar);
  }

  /* brand side */
  .brand-mark {
    position: absolute; left: -2px; top: 3px; width: 414px; height: 414px;
    border-radius: 50%; background: var(--navy);
  }
  .card--brand .clinic-name {
    left: 440px; top: 124px; font-size: 28px; letter-spacing: 4px;
  }
  .brand-web {
    position: absolute; left: 438px; top: 259px;
    font-size: 16.5px; color: var(--ink); white-space: nowrap;
  }
  .brand-web strong { font-weight: 600; color: var(--navy); }
  .brand-web .accent { font-weight: 600; color: var(--teal); }
</style>
</head>
<body>
<main class="canvas">

  <section class="card card--contact">
    <div class="clinic-mark"></div>
    <div class="clinic-name">Marrow Bend<br>Eye Care<br>Optometry</div>

    <h1 class="person-name">DR LENA QUORVIK</h1>
    <p class="person-title">OPTOMETRIST</p>
    <div class="rule-strong"></div>
    <div class="rule-thin"></div>

    <p class="contact contact--phone">
      <svg viewBox="0 0 16 16" aria-hidden="true"><circle cx="8" cy="8" r="7" fill="none" stroke="#0355a3" stroke-width="1.3"/><path d="M5.5 4.5l1.5 0 .6 2-1 .8c.5 1.2 1.2 1.9 2.2 2.3l.8-1 2 .6v1.5c-3.5.2-6.3-2.7-6.1-6.2z" fill="#0355a3"/></svg>
      604-319-2058
    </p>
    <p class="contact contact--email">
      <svg viewBox="0 0 16 16" aria-hidden="true"><rect x="1" y="5" width="14" height="9" rx="1" fill="#0355a3"/><path d="M1.5 5.5L8 10l6.5-4.5" fill="none" stroke="#fff" stroke-width="1.2"/><path d="M3 5L8 1.5 13 5" fill="none" stroke="#0355a3" stroke-width="1.2"/></svg>
      info@marrowbendeyecare.com
    </p>
    <p class="contact contact--web">
      <svg viewBox="0 0 16 16" aria-hidden="true"><g fill="none" stroke="#0355a3" stroke-width="1.1"><circle cx="8" cy="8" r="7"/><ellipse cx="8" cy="8" rx="3" ry="7"/><path d="M1 8h14M2.2 4.5h11.6M2.2 11.5h11.6"/></g></svg>
      www.marrowbendeyecare.com
    </p>

    <div class="contact-divider"></div>
    <div class="contact contact--address">
      <svg viewBox="0 0 16 16" aria-hidden="true"><circle cx="8" cy="8" r="7" fill="none" stroke="#0355a3" stroke-width="1.3"/><path d="M8 3.5a2.8 2.8 0 0 1 2.8 2.8c0 2-2.8 5.2-2.8 5.2S5.2 8.3 5.2 6.3A2.8 2.8 0 0 1 8 3.5z" fill="#0355a3"/><circle cx="8" cy="6.3" r="1" fill="#fff"/></svg>
      <div><span>217-392 E Halvering Ave</span><span>Vancouver BC V6R 3J8</span></div>
    </div>

    <div class="card-band"></div>
  </section>

  <section class="card card--brand">
    <div class="brand-mark"></div>
    <div class="clinic-name">Marrow Bend<br>Eye Care<br>Optometry</div>
    <p class="brand-web">www.<strong>marrowbend</strong><span class="accent">eyecare</span>.com</p>
  </section>

</main>
</body>
</html>
```